Rack Flyer for Willowmere Dementia

We need a rack flyer design providing information on services we offer, fees and relevant contact information. Using company branding (logo, font and colours). Must be provided in a format that is easily edited for ongoing use.

For DL size (99 x 210mm)

```html
<!DOCTYPE html>
<html lang="en">
<head>
<meta charset="utf-8">
<title>Willowmere Dementia – Rack Flyer</title>
<link href="https://fonts.googleapis.com/css2?family=Didact+Gothic&family=Montserrat:wght@600;700&family=Dancing+Script:wght@600;700&display=swap" rel="stylesheet">
<style>
  :root{
    --navy:#1f2a6b;
    --orange:#f7941d;
    --stage:#c9cdd0;
    --white:#ffffff;
    --ink:#3a3a3a;
  }
  *{margin:0;padding:0;box-sizing:border-box}
  html,body{width:1200px;height:1200px;overflow:hidden;background:var(--stage)}
  body{position:relative;font-family:"Didact Gothic",sans-serif;color:var(--ink)}
  .flyer{position:absolute;top:91px;width:481px;height:1020px;background:var(--white);overflow:hidden}
  .flyer--front{left:81px}
  .flyer--back{left:632px}
  .abs{position:absolute}
  .wave{position:absolute;left:0;width:481px}
  .script{font-family:"Dancing Script",cursive;font-weight:700}

  /* front */
  .brand{top:30px;left:0;width:481px;display:flex;align-items:center;justify-content:center;gap:12px}
  .brand__dot{width:34px;height:34px;border-radius:50%;background:var(--navy)}
  .brand__name{font-family:"Montserrat",sans-serif;font-weight:700;font-size:30px;color:var(--navy);letter-spacing:-.3px}
  .hero-photo{top:92px;left:0;width:481px;height:300px;background:linear-gradient(135deg,#e9b98f 0%,#8fa7d6 40%,#f2a23c 100%)}
  .portrait{top:226px;left:240px;width:222px;height:222px;border-radius:50%;border:5px solid var(--white);background:radial-gradient(circle at 50% 40%,#7a5440,#3a2a24 70%);z-index:3}
  .intro-head{top:350px;left:64px;width:180px;text-align:center;font-family:"Montserrat",sans-serif;font-weight:700;font-size:19.5px;line-height:1.22;color:var(--navy);z-index:3}
  .intro-body{top:463px;left:0;width:481px;text-align:center;font-size:18.5px;line-height:22.5px;white-space:nowrap}
  .tagline{top:530px;left:0;width:481px;text-align:center;font-size:37px;line-height:46px;color:var(--orange)}
  .mission{top:586px;left:0;width:481px;text-align:center;font-size:18.5px;line-height:23.5px;white-space:nowrap}
  .mission strong{font-family:"Montserrat",sans-serif;font-weight:700;color:var(--navy);font-size:17px;border-bottom:1.5px solid var(--orange)}
  .goal{top:759px;left:11px;width:459px;height:190px;border-radius:50%;background:var(--navy);z-index:3;color:var(--white);text-align:center;padding-top:10px}
  .goal__title{font-size:30px;line-height:38px;color:var(--white)}
  .goal__title span{color:var(--orange);font-size:18px;vertical-align:middle}
  .goal__text{font-family:"Montserrat",sans-serif;font-weight:600;font-size:16px;line-height:23px;white-space:nowrap}
  .front-footer{top:957px;left:0;width:481px;text-align:center;z-index:4}
  .front-footer__line{font-family:"Montserrat",sans-serif;font-weight:600;font-size:18.5px;line-height:25px;color:var(--white)}
  .front-footer__url{font-family:"Montserrat",sans-serif;font-weight:700;font-size:17px;line-height:24px;color:var(--navy)}
  .rule{top:969px;width:62px;height:2px;background:var(--white);z-index:4}
  .rule--left{left:15px}
  .rule--right{left:404px}

  /* back */
  .care-photo{top:0;left:0;width:481px;height:250px;background:linear-gradient(120deg,#b9b1a9 0%,#e6e2dd 45%,#f4f4f2 70%,#c8cfd2 100%)}
  .services-title{top:226px;left:0;width:481px;text-align:center;font-size:33px;line-height:42px;color:var(--navy)}
  .services-title span{color:var(--orange);font-size:20px;vertical-align:middle}
  .services{top:278px;left:18px;width:450px;list-style:none;font-size:17px;line-height:20.2px;white-space:nowrap}
  .services li{position:relative;padding-left:13px}
  .services li::before{content:"";position:absolute;left:0;top:8px;width:6px;height:6px;border-radius:50%;background:var(--orange)}
  .brain-icon{top:390px;left:384px;width:84px;height:62px;border-radius:40% 40% 35% 35%;background:var(--orange)}
  .fees-pill{top:555px;left:140px;width:202px;height:34px;border-radius:17px;background:var(--navy);color:var(--white);font-family:"Montserrat",sans-serif;font-weight:600;font-size:20px;text-align:center;line-height:34px;z-index:2}
  .fees{top:604px;left:0;width:481px;list-style:none;z-index:2}
  .fees li{display:flex;align-items:flex-start;gap:9px;font-family:"Montserrat",sans-serif;font-weight:700;font-size:16px;line-height:24px;color:var(--navy)}
  .fees .price{flex:none;background:var(--white);color:var(--orange);border-radius:0 12px 12px 0;padding:0 8px 0 4px;height:19px;line-height:19px;margin-top:3px;font-size:15.5px;min-width:70px}
  .fees .price--wide{min-width:135px}
  .coverage{top:762px;left:14px;width:453px;color:var(--white);font-size:16.5px;line-height:23px;text-align:justify;z-index:2}
  .reach{top:912px;left:0;width:481px;text-align:center;color:var(--white);font-family:"Montserrat",sans-serif;font-weight:600;font-size:15.5px;z-index:2}
  .url-pill{top:949px;left:74px;width:334px;height:34px;border-radius:17px;background:var(--navy);color:var(--white);font-family:"Montserrat",sans-serif;font-weight:700;font-size:17px;text-align:center;line-height:34px;z-index:3}
  .contact{top:992px;left:0;width:481px;text-align:center;font-family:"Montserrat",sans-serif;font-weight:700;font-size:17px;color:var(--navy);z-index:3}
  .contact .sep{color:var(--orange);margin:0 6px}
</style>
</head>
<body>

<section class="flyer flyer--front">
  <div class="abs brand">
    <span class="brand__dot"></span>
    <span class="brand__name">Willowmere Dementia</span>
  </div>

  <div class="abs hero-photo" role="img" aria-label="Photograph of open hands holding forget-me-not flowers and a stone engraved with the word hope"></div>

  <svg class="wave" style="top:300px;z-index:2" height="120" viewBox="0 0 481 120" aria-hidden="true">
    <path d="M0,30 Q200,-10 481,10 L481,120 L0,120Z" fill="var(--white)"/>
  </svg>

  <div class="abs portrait" role="img" aria-label="Photograph of an older person holding their head in their hands, looking worried"></div>

  <h1 class="abs intro-head">Navigating a diagnosis of dementia can be daunting…</h1>

  <p class="abs intro-body">You likely have many questions, and it can be<br>overwhelming trying to figure out where to turn to<br>for answers &amp; help. We want you to know that</p>

  <p class="abs tagline script">You're not alone in this journey</p>

  <p class="abs mission">As the numbers of those living with dementia<br>in Bermuda continue to rise placing greater<br>demands on an already strained health care<br>system, Willowmere's clinical &amp; evidence based<br>consultation services improve the<br><strong>safety, independence and quality of life</strong><br>of persons with dementia and their caregivers.</p>

  <svg class="wave" style="top:800px" height="220" viewBox="0 0 481 220" aria-hidden="true">
    <path d="M0,20 Q240,-10 481,50 L481,220 L0,220Z" fill="var(--orange)"/>
  </svg>

  <div class="abs goal">
    <p class="goal__title script"><span>★</span> Our Goal <span>★</span></p>
    <p class="goal__text">to assist clients to successfully age<br>in place at home with the support of their<br>family caregivers to reduce the overall<br>cost &amp; burden of care for this<br>vulnerable population.</p>
  </div>

  <div class="abs rule rule--left"></div>
  <div class="abs rule rule--right"></div>
  <div class="abs front-footer">
    <p class="front-footer__line">Navigating Dementia Together</p>
    <p class="front-footer__url">www.willowmeredementia.bm</p>
  </div>
</section>

<section class="flyer flyer--back">
  <div class="abs care-photo" role="img" aria-label="Photograph of a smiling carer looking through a photo album with an elderly woman"></div>

  <svg class="wave" style="top:190px" height="80" viewBox="0 0 481 80" aria-hidden="true">
    <path d="M0,48 Q200,22 481,8 L481,80 L0,80Z" fill="var(--white)"/>
    <path d="M0,48 Q200,22 481,8" fill="none" stroke="var(--orange)" stroke-width="5"/>
  </svg>

  <h2 class="abs services-title script"><span>★</span> Services Offered <span>★</span></h2>

  <ul class="abs services">
    <li>Comprehensive Dementia Assessment</li>
    <li>Cognitive/Perceptual Screening</li>
    <li>Home Safety Audit<br>(Home modifications &amp; adaptive equipment aids)</li>
    <li>Caregiver Education &amp; Support</li>
    <li>Falls Prevention Strategies</li>
    <li>Personalised Care Planning</li>
    <li>Preparation for future disease progression</li>
    <li>Case Management Support</li>
    <li>Check-in/monitoring visits for clients with<br>limited social support</li>
    <li>Cognitive Stimulation Therapy (group program<br>for individuals with mild-moderate stage dementia)</li>
  </ul>

  <div class="abs brain-icon" role="img" aria-label="Orange brain icon"></div>

  <svg class="wave" style="top:540px" height="400" viewBox="0 0 481 400" aria-hidden="true">
    <path d="M0,24 Q240,-8 481,8 L481,400 L0,400Z" fill="var(--orange)"/>
  </svg>

  <div class="abs fees-pill">SERVICE FEES</div>

  <ul class="abs fees">
    <li><span class="price">$180</span>Initial Consultation</li>
    <li><span class="price">$395</span>Comprehensive Dementia Assessment</li>
    <li><span class="price">$720</span>Comprehensive Dementia Assessment<br>&amp; ongoing case management services</li>
    <li><span class="price">$180</span>Monthly check in/monitoring visits</li>
    <li><span class="price price--wide">$500 per term</span>Cognitive Stimulation Therapy</li>
  </ul>

  <p class="abs coverage">We are pleased to share that services offered by Willowmere Dementia are currently covered under Harbourline &amp; Keystone health insurance plans. We also have availability of funding support for those in financial need who are unable to afford co-pay, enabling equitable access to these essential care and support services regardless of financial means.</p>

  <p class="abs reach">Please feel free to reach out for further information.</p>

  <div class="abs url-pill">www.willowmeredementia.bm</div>

  <p class="abs contact">(441) 555 0142<span class="sep">|</span>info@willowmeredementia.bm</p>
</section>

</body>
</html>
```